Basisdesign Buch-/E-Book-Cover für Haldmoor-Krimis
Zielgruppe
Ich schreibe Krimis, Thriller, Kriminalstories, Krimiparodien.
Meine Zielgruppe sind deutschsprachige Krimi-Leser.
Aufgabenstellung
Ich benötige ein Basisdesign für Buchcover (Höhe 2.343, Breite 1.518 Pixel – Druckfalter, eBooks). Alle Bücher haben mit Crime zu tun, aber in verschiedenen Unter-Genres: Klassischer Kriminalroman, Thriller, Fantasy Thriller, Kurzgeschichten, Krimi-Parodien.
Ich benötige, quasi als Marke, dafür ein gleichbleibendes grafisches Element, z. B. einen Sockel im unteren Coverbereich, der den Autorennamen „Jonas Haldmoor“ und das jeweilige Unter-Genre enthält. Unter-Genres sind: Krimi, Thriller, Fantasy-Thriller, Kurzgeschichten und Krimi-Parodie. Das alles sollte auch noch im Format der Lesoria-Bücherlisten wie „Kunden kauften auch“ halbwegs lesbar sein.
Ein bisschen mörderisch und blutig sind alle Varianten.
Nachdem die Bandbreite vom Thriller bis zur Parodie reicht, sollte der gleichbleibende Markenbereich eine entsprechende grafische Bandbreite aufweisen, dabei aber die Grundmelodie Crime nicht aus den Augen verlieren.
Im oberen Bereich stelle ich mir Grafiken oder Hintergrundfotos vor, die für jedes Buch individuell gestaltet werden müssten, was jedoch über das Basisdesign hinausgeht. Die Wahl der Schriftart für Titel (bislang 11 – 25 Zeichen inkl. Leerzeichen) und allfällige Untertitel (im Umfang von maximal 30 Zeichen), sollte zu denen im Sockel passen.

```html
<!DOCTYPE html>
<html lang="de">
<head>
<meta charset="utf-8">
<title>Haldmoor-Krimis – Basisdesign Buchcover</title>
<link rel="stylesheet" href="https://fonts.googleapis.com/css2?family=Oswald:wght@500;700&family=EB+Garamond:ital,wght@0,500;1,500&display=swap">
<style>
  :root {
    --page-bg: #e9e8e4;
    --ink-black: #111111;
    --crime-red: #d9181b;
    --title-red: #e0201f;
    --parody-yellow: #f2c11a;
    --title-yellow: #f7c51c;
    --fantasy-cyan: #1fc2ec;
    --title-cyan: #27c6f2;
    --deep-blue: #12337a;
    --paper-white: #f7f6f2;
    --name-white: #ffffff;
    --genre-dark: #2a1a12;
  }
  * { box-sizing: border-box; margin: 0; padding: 0; }
  html, body { width: 1200px; height: 800px; overflow: hidden; }
  body {
    background: var(--page-bg);
    display: flex;
    align-items: center;
    justify-content: center;
  }
  .cover-series {
    display: flex;
    gap: 26px;
  }
  .cover {
    position: relative;
    width: 208px;
    height: 321px;
    overflow: hidden;
    background: var(--ink-black);
    box-shadow: 0 6px 16px rgba(0,0,0,.25);
  }
  .cover__art {
    position: absolute;
    inset: 0;
  }
  .cover__title {
    position: absolute;
    left: 10px;
    right: 10px;
    top: 26px;
    font-family: "Oswald", "Arial Narrow", sans-serif;
    font-weight: 700;
    text-transform: uppercase;
    line-height: 1.05;
    letter-spacing: .5px;
    text-align: center;
    transform: rotate(-4deg);
  }
  .cover__title-line { display: block; font-size: 29px; white-space: nowrap; }
  .cover__subtitle {
    display: block;
    margin-top: 8px;
    font-family: "Oswald", "Arial Narrow", sans-serif;
    font-weight: 500;
    font-size: 14px;
    line-height: 1.2;
    text-align: center;
    white-space: nowrap;
  }

  /* Markenbereich: gerissener Sockel */
  .brand-plinth {
    position: absolute;
    left: -14px;
    right: -14px;
    top: 208px;
    height: 86px;
    transform: rotate(-4deg);
  }
  .brand-plinth__paper {
    position: absolute;
    inset: 0;
    background: var(--paper-white);
    clip-path: polygon(0% 8%, 4% 3%, 8% 9%, 12% 2%, 17% 7%, 21% 1%, 26% 8%, 31% 3%, 35% 9%, 40% 2%, 45% 6%, 50% 0%, 55% 7%, 60% 2%, 64% 8%, 69% 1%, 74% 6%, 79% 2%, 83% 9%, 88% 3%, 93% 7%, 97% 1%, 100% 6%,
      100% 94%, 96% 99%, 91% 92%, 86% 98%, 81% 93%, 76% 100%, 71% 94%, 66% 99%, 61% 92%, 56% 98%, 51% 93%, 46% 100%, 41% 94%, 36% 98%, 31% 91%, 26% 99%, 21% 93%, 16% 98%, 11% 92%, 6% 99%, 0% 93%);
  }
  .brand-plinth__band {
    position: absolute;
    inset: 5px 0 5px 0;
    clip-path: polygon(0% 6%, 5% 1%, 9% 8%, 14% 2%, 19% 9%, 23% 3%, 28% 7%, 33% 0%, 38% 8%, 42% 3%, 47% 9%, 52% 2%, 57% 6%, 62% 0%, 67% 8%, 71% 3%, 76% 9%, 81% 1%, 86% 7%, 90% 2%, 95% 8%, 100% 3%,
      100% 96%, 95% 91%, 90% 99%, 85% 93%, 80% 100%, 75% 92%, 70% 97%, 65% 91%, 60% 99%, 55% 94%, 50% 100%, 45% 92%, 40% 98%, 35% 93%, 30% 100%, 25% 92%, 20% 98%, 15% 91%, 10% 99%, 5% 93%, 0% 98%);
  }
  .brand-plinth__genre {
    position: absolute;
    left: 0;
    right: 0;
    top: 16px;
    text-align: center;
    font-family: "EB Garamond", "Times New Roman", serif;
    font-style: italic;
    font-weight: 500;
    font-size: 12px;
    color: var(--genre-dark);
  }
  .brand-plinth__author {
    position: absolute;
    left: 0;
    right: 0;
    top: 32px;
    text-align: center;
    font-family: "EB Garamond", "Times New Roman", serif;
    font-weight: 500;
    font-size: 25px;
    letter-spacing: -.3px;
    color: var(--name-white);
  }

  .band--crime { background: var(--crime-red); }
  .band--parody { background: var(--parody-yellow); }
  .band--fantasy { background: var(--fantasy-cyan); }

  /* Einzelcover */
  .cover--haselnuss .cover__title { color: var(--title-red); }
  .cover--haselnuss .cover__art {
    background: radial-gradient(ellipse 70% 30% at 45% 66%, #f39a1c 0%, #c2420e 40%, rgba(17,17,17,0) 75%), var(--ink-black);
  }
  .cover--gaukler .cover__title { color: var(--title-red); }
  .cover--gaukler .cover__art {
    background: radial-gradient(ellipse 45% 26% at 50% 58%, #b8923a 0%, #6b5120 45%, rgba(17,17,17,0) 80%), var(--ink-black);
  }
  .cover--toten .cover__art {
    background: linear-gradient(180deg, #c9dbe8 0%, #9fb9cc 35%, #6f8a7a 58%, #4f6a44 72%, #8aa56a 100%);
  }
  .cover--toten .cover__title {
    color: var(--title-red);
    transform: none;
    top: 16px;
    line-height: 1;
  }
  .cover--toten .cover__title-line { font-size: 50px; }
  .cover--toten .cover__title-line--small { font-size: 34px; margin: 2px 0; }
  .cover--liebe .cover__art {
    background: radial-gradient(ellipse 55% 18% at 45% 58%, #e8b39c 0%, #a36e5c 50%, rgba(17,17,17,0) 85%), var(--ink-black);
  }
  .cover--liebe .cover__title { color: var(--title-yellow); transform: none; top: 20px; line-height: 1.02; }
  .cover--liebe .cover__title-line { font-size: 56px; }
  .cover--moretti .cover__art {
    background: linear-gradient(180deg, var(--deep-blue) 0%, #2a5aa8 30%, #c9d8e6 45%, #c9824a 55%, #3f8a8e 66%, #1e6fa0 100%);
  }
  .cover--moretti .cover__title { color: var(--title-cyan); transform: none; top: 20px; line-height: 1.02; }
  .cover--moretti .cover__title-line { font-size: 40px; }
  .cover--moretti .cover__subtitle { font-size: 14px; margin-top: 4px; }
</style>
</head>
<body>
  <main class="cover-series">

    <article class="cover cover--haselnuss">
      <div class="cover__art" role="img" aria-label="Flammen auf schwarzem Grund"></div>
      <h2 class="cover__title">
        <span class="cover__title-line">Das Lied der</span>
        <span class="cover__title-line">Haselnuss</span>
        <span class="cover__subtitle">Oberinspektor Brandts<br>Hexenjagd</span>
      </h2>
      <div class="brand-plinth">
        <div class="brand-plinth__paper"></div>
        <div class="brand-plinth__band band--crime"></div>
        <p class="brand-plinth__genre">Kriminalroman</p>
        <p class="brand-plinth__author">Jonas Haldmoor</p>
      </div>
    </article>

    <article class="cover cover--gaukler">
      <div class="cover__art" role="img" aria-label="Goldene venezianische Masken im Dunkeln"></div>
      <h2 class="cover__title">
        <span class="cover__title-line">Zirkel der</span>
        <span class="cover__title-line">Gaukler</span>
        <span class="cover__subtitle">Oberinspektor Brandt<br>in Graz</span>
      </h2>
      <div class="brand-plinth">
        <div class="brand-plinth__paper"></div>
        <div class="brand-plinth__band band--crime"></div>
        <p class="brand-plinth__genre">Kriminalroman</p>
        <p class="brand-plinth__author">Jonas Haldmoor</p>
      </div>
    </article>

    <article class="cover cover--toten">
      <div class="cover__art" role="img" aria-label="Alpental mit Bergen, Wald und Dorfkirche"></div>
      <h2 class="cover__title">
        <span class="cover__title-line">Tal</span>
        <span class="cover__title-line cover__title-line--small">der</span>
        <span class="cover__title-line">Toten</span>
      </h2>
      <div class="brand-plinth">
        <div class="brand-plinth__paper"></div>
        <div class="brand-plinth__band band--crime"></div>
        <p class="brand-plinth__genre">Ein Kärnten-Thriller</p>
        <p class="brand-plinth__author">Jonas Haldmoor</p>
      </div>
    </article>

    <article class="cover cover--liebe">
      <div class="cover__art" role="img" aria-label="Liegende rothaarige Frau, von hinten gesehen, auf grünem Tuch"></div>
      <h2 class="cover__title">
        <span class="cover__title-line">Runde</span>
        <span class="cover__title-line">Liebe</span>
      </h2>
      <div class="brand-plinth">
        <div class="brand-plinth__paper"></div>
        <div class="brand-plinth__band band--parody"></div>
        <p class="brand-plinth__genre">irrwitzige Krimistories</p>
        <p class="brand-plinth__author">Jonas Haldmoor</p>
      </div>
    </article>

    <article class="cover cover--moretti">
      <div class="cover__art" role="img" aria-label="Italienische Altstadt mit Brücke über den Fluss unter blauem Himmel"></div>
      <h2 class="cover__title">
        <span class="cover__title-line">Elena</span>
        <span class="cover__title-line">Moretti</span>
        <span class="cover__subtitle">Das Zeitenband</span>
      </h2>
      <div class="brand-plinth">
        <div class="brand-plinth__paper"></div>
        <div class="brand-plinth__band band--fantasy"></div>
        <p class="brand-plinth__genre">Fantasy-Thriller</p>
        <p class="brand-plinth__author">Jonas Haldmoor</p>
      </div>
    </article>

  </main>
</body>
</html>
```